Kegelhof Sports- & Billardbar

Hello,
I Need a Plauderbuch-Design for my Sports- & Billardbar.
It should include a Profile Picture and a title Picture (Banner).
The following Information should be included in the banner:

"Official Logo (attached)

5 Pool-Billard Tische
3 Snooker Tische
3 Dart-Automaten
1 Tischkicker

1 Großbildleinwand
4 TV-Geräte
2 Wolkra-Leitungen
Alle Sportevents LIVE & in HD

Kegelhof, Lindenweg 14, 70599 Talbach"

I have attached the Logo and some Pictures, which can be used, but don`t have to. You can just try them out. They are not best Quality though.
I have also attached the Logo of the Torrunde, Meisterpokal Serie, etc.
This Logos should get included!

The corporate Colors are the same than the official "Kegelhof"-Logo.

If you have any questions, just contact me!

Thanks in Advance!

Torsten

Reason: Project Needs more time to realize, I think!

```html
<!DOCTYPE html>
<html lang="de">
<head>
<meta charset="utf-8">
<title>Kegelhof – Plauderbuch Titelbild</title>
<link rel="stylesheet" href="https://fonts.googleapis.com/css2?family=Archivo+Black&family=Alfa+Slab+One&family=Ubuntu:wght@500;700&family=Roboto+Slab:wght@800&display=swap">
<style>
  :root{
    --ink:#1b1b1d;
    --navy:#0e1a30;
    --red:#e3141b;
    --white:#ffffff;
    --grey:#3a3a3a;
    --glow:#7fc8ff;
    --field-light:#eef3ea;
    --field-mid:#cfe0c4;
    --field-dark:#8fb07f;
    --photo-warm:#6b4a32;
    --photo-warm-dark:#2a1c14;
    --photo-bar:#7a1e26;
    --photo-bar-dark:#2b0d12;
    --badge-red:#d5232a;
    --badge-orange:#e47b1d;
    --badge-grey:#b9bcc2;
  }
  html,body{margin:0;padding:0;overflow:hidden;background:var(--white);}
  .banner{
    position:relative;width:1200px;height:444px;overflow:hidden;
    font-family:"Ubuntu",sans-serif;
  }
  .banner__background{
    position:absolute;inset:0;
    background:
      radial-gradient(ellipse at 30% 60%, rgba(255,255,255,.85) 0%, rgba(255,255,255,0) 55%),
      linear-gradient(180deg,var(--field-light) 0%,var(--field-mid) 55%,var(--field-dark) 100%);
  }
  .brand{position:absolute;left:106px;top:8px;width:1016px;height:86px;}
  .brand__name{font-family:"Archivo Black",sans-serif;font-size:106px;fill:var(--ink);}
  .brand__tagline{
    position:absolute;left:706px;top:96px;width:416px;
    font-family:"Ubuntu",sans-serif;font-weight:500;font-size:17px;
    letter-spacing:4.6px;color:var(--grey);white-space:nowrap;
  }
  .headline{position:absolute;left:4px;top:112px;width:712px;height:50px;margin:0;}
  .headline__text{
    font-family:"Alfa Slab One",serif;font-size:36px;fill:var(--red);
    stroke:var(--white);stroke-width:6px;paint-order:stroke fill;stroke-linejoin:round;
  }
  .features{
    position:absolute;left:216px;top:166px;width:400px;margin:0;padding:0;list-style:none;
    text-align:center;
  }
  .features__item{
    font-family:"Ubuntu",sans-serif;font-weight:700;font-size:28px;line-height:38.5px;
    color:var(--navy);white-space:nowrap;
    -webkit-text-stroke:6px var(--white);paint-order:stroke fill;
    text-shadow:0 0 6px var(--glow),0 0 10px var(--glow);
  }
  .profile-slot{position:absolute;left:40px;top:282px;width:225px;height:162px;background:#000;}
  .photo{
    position:absolute;margin:0;background:var(--white);padding:9px;
    box-shadow:2px 4px 8px rgba(0,0,0,.4);
  }
  .photo__image{width:100%;height:100%;}
  .photo--lounge{left:706px;top:142px;width:166px;height:194px;transform:rotate(-3deg);}
  .photo--lounge .photo__image{background:linear-gradient(160deg,var(--photo-warm) 0%,#a07a55 45%,var(--photo-warm-dark) 100%);}
  .photo--tables{left:922px;top:130px;width:188px;height:190px;transform:rotate(3.5deg);}
  .photo--tables .photo__image{background:linear-gradient(170deg,var(--photo-bar) 0%,#4a2030 45%,#1f6b5a 80%,var(--photo-bar-dark) 100%);}
  .partners{position:absolute;left:562px;top:378px;width:285px;height:62px;}
  .address{position:absolute;left:856px;top:410px;width:340px;height:24px;margin:0;}
  .address__text{
    font-family:"Roboto Slab",serif;font-weight:800;font-size:14px;fill:var(--ink);
    stroke:var(--white);stroke-width:3px;paint-order:stroke fill;
  }
</style>
</head>
<body>
<main class="banner">
  <div class="banner__background" role="img" aria-label="Fußballfeld mit Ball und Tornetz im Hintergrund"></div>

  <svg class="brand" viewBox="0 0 1016 86" aria-label="Kegelhof">
    <text class="brand__name" x="0" y="84" textLength="1014" lengthAdjust="spacingAndGlyphs">KEGELHOF</text>
  </svg>
  <div class="brand__tagline">BILLARD - SPORTSBAR - LOUNGE</div>

  <svg class="headline" viewBox="0 0 712 50" role="heading" aria-level="1" aria-label="All Sportevents LIVE &amp; in HD">
    <text class="headline__text" x="4" y="40" textLength="698" lengthAdjust="spacingAndGlyphs">All Sportevents LIVE &amp; in HD</text>
  </svg>

  <ul class="features">
    <li class="features__item">5 Pool-Billard Tische</li>
    <li class="features__item">3 Snooker Tische</li>
    <li class="features__item">3 Dart-Automaten</li>
    <li class="features__item">1 Tischkicker</li>
    <li class="features__item">1 Großbildleinwand</li>
    <li class="features__item">4 TV-Geräte</li>
    <li class="features__item">2 Wolkra-Leitungen</li>
  </ul>

  <div class="profile-slot" role="img" aria-label="Platz für das Profilbild"></div>

  <figure class="photo photo--lounge">
    <div class="photo__image" role="img" aria-label="Foto der Lounge mit Bar und Sitzgruppen"></div>
  </figure>
  <figure class="photo photo--tables">
    <div class="photo__image" role="img" aria-label="Foto des Billardraums mit Pooltischen"></div>
  </figure>

  <svg class="partners" viewBox="0 0 285 62" role="img" aria-label="Wettbewerbs-Abzeichen: Torrunde, Europapokal, Meisterpokal Serie, Pokal">
    <rect x="2" y="6" width="56" height="52" rx="4" fill="var(--badge-red)"/>
    <circle cx="106" cy="32" r="26" fill="var(--badge-orange)"/>
    <circle cx="176" cy="32" r="26" fill="var(--badge-grey)"/>
    <circle cx="250" cy="30" r="29" fill="var(--white)" stroke="var(--badge-grey)" stroke-width="3"/>
  </svg>

  <svg class="address" viewBox="0 0 340 24" aria-label="Kegelhof, Lindenweg 14, 70599 Talbach">
    <text class="address__text" x="1" y="18" textLength="336" lengthAdjust="spacingAndGlyphs">Kegelhof, Lindenweg 14, 70599 Talbach</text>
  </svg>
</main>
</body>
</html>
```